Student Business Card Design

As you already know, I'm a student at BV majoring in Supply Chain & Logistics Technology. I want a business card design that leaves the recipient impressed. A clean, professional, and memorable design is desired without too much color. My school's logo can be found online. I'd like to have that on the card.

Target Market(s)

Anyone who is a recruiter or an employer who has authority to hire.

Industry/Entity Type

Business

Contact Information for Business Card

Name: Osman Velibor

Phone Number: 614-275-3316

Email Address: velibor.osman@mailbox-demo.net

Major: Supply Chain & Logistics Technology

Minor: Purchasing

University: Marlowe State University

College: Ashcombe School of Engineering

I want a Workvine logo with my name beside it.

Also, on the back of the card I want this quote: "If it doesn't challenge you, it doesn't change you"-, Lena Sorbach

Requirements
Must have
• I'd like to see a Workvine logo go with my name.
• Professional-I'm going to be handing this card out in career fairs and networking events.
Nice to have
• Marlowe State University's colors: white, silver, and red, but if you feel it's better to go with a different color scheme then do it.
Should not have
• No white space on the design.

```html
<!DOCTYPE html>
<html lang="en">
<head>
<meta charset="UTF-8">
<title>Osman Velibor – Business Card</title>
<link rel="stylesheet" href="https://fonts.googleapis.com/css2?family=Jost:wght@400;500;700&display=swap">
<style>
  :root {
    --page-bg: #d9d9d9;
    --silver-light: #f2f2f2;
    --silver-mid: #cfcfcf;
    --silver-dark: #b5b5b5;
    --red: #c8141c;
    --red-dark: #8e0a10;
    --ink: #222222;
    --white: #ffffff;
  }
  html, body {
    margin: 0;
    width: 1200px;
    height: 998px;
    overflow: hidden;
    background: var(--page-bg);
    font-family: "Jost", sans-serif;
  }
  .card {
    position: absolute;
    left: 80px;
    top: 202px;
    width: 1040px;
    height: 594px;
    background: linear-gradient(100deg, var(--silver-dark) 0%, var(--silver-light) 45%, var(--silver-mid) 70%, var(--silver-light) 100%);
    box-shadow: 0 10px 30px rgba(0,0,0,0.25);
    overflow: hidden;
  }
  .school {
    position: absolute;
    left: 40px;
    top: 30px;
    color: var(--ink);
    font-size: 21px;
    line-height: 1.9;
  }
  .monogram {
    position: absolute;
    left: 0;
    right: 0;
    top: 18px;
    text-align: center;
    color: var(--red);
    font-size: 120px;
    font-weight: 700;
    line-height: 1;
    z-index: 2;
  }
  .study {
    position: absolute;
    right: 40px;
    top: 38px;
    color: var(--ink);
    font-size: 21px;
    line-height: 1.3;
  }
  .study-indent { padding-left: 72px; }
  .name-band {
    position: absolute;
    left: 0;
    right: 0;
    top: 150px;
    height: 110px;
    background: linear-gradient(90deg, var(--red-dark), var(--red) 50%, var(--red-dark));
    display: flex;
    align-items: center;
    justify-content: center;
    gap: 14px;
  }
  .name {
    color: var(--white);
    font-size: 58px;
    font-weight: 700;
    letter-spacing: 1px;
  }
  .network {
    display: flex;
    align-items: center;
    gap: 6px;
    color: var(--white);
    font-size: 20px;
    font-weight: 700;
    margin-top: 26px;
  }
  .network-square {
    width: 14px;
    height: 14px;
    background: var(--white);
  }
  .contact {
    position: absolute;
    left: 0;
    right: 0;
    top: 280px;
  }
  .contact-row {
    height: 62px;
    display: flex;
    align-items: center;
    justify-content: center;
    gap: 20px;
    color: var(--red-dark);
    font-size: 42px;
    line-height: 62px;
  }
  .contact-icon {
    flex: none;
  }
  .quote-band {
    position: absolute;
    left: 0;
    right: 0;
    top: 420px;
    bottom: 0;
    background: linear-gradient(90deg, var(--red-dark), var(--red) 50%, var(--red-dark));
    color: var(--white);
  }
  .quote {
    margin: 28px 0 0 50px;
    font-size: 32px;
  }
  .quote-author {
    position: absolute;
    right: 70px;
    bottom: 28px;
    font-size: 32px;
  }
</style>
</head>
<body>
  <div class="card">
    <div class="school">
      <div class="school-name">Marlowe State University</div>
      <div class="school-college">Ashcombe School of Engineering</div>
    </div>

    <div class="monogram">BV</div>

    <div class="study">
      <div>Major: Supply Chain &amp;</div>
      <div class="study-indent">Logistics Technology</div>
      <div>Minor: Purchasing</div>
    </div>

    <div class="name-band">
      <span class="name">Osman Velibor</span>
      <span class="network"><span class="network-square"></span>Workvine</span>
    </div>

    <div class="contact">
      <div class="contact-row">
        <svg class="contact-icon" width="24" height="36" viewBox="0 0 24 36" aria-hidden="true">
          <rect x="2" y="2" width="20" height="32" rx="3" fill="none" stroke="var(--red-dark)" stroke-width="2.5"/>
          <line x1="9" y1="29" x2="15" y2="29" stroke="var(--red-dark)" stroke-width="2.5"/>
        </svg>
        <span class="contact-text">614-275-3316</span>
      </div>
      <div class="contact-row">
        <svg class="contact-icon" width="42" height="30" viewBox="0 0 42 30" aria-hidden="true">
          <rect x="1" y="1" width="40" height="28" fill="var(--red-dark)"/>
          <polyline points="1,1 21,17 41,1" fill="none" stroke="var(--silver-light)" stroke-width="2"/>
        </svg>
        <span class="contact-text">velibor.osman@mailbox-demo.net</span>
      </div>
    </div>

    <div class="quote-band">
      <p class="quote">"If it doesn't challenge you, it doesn't change you"</p>
      <div class="quote-author">- Lena Sorbach</div>
    </div>
  </div>
</body>
</html>
```